meridale partners business card

Architectural firm business card
Updates

Please note:

corporate colour black+yellow are the only elements to be kept.
NO OTHER ELEMENT TO BE REUSED FROM PREVIOUS BUSINESS CARD.
Thank you.

Dear Everyone,

Thank you for your participation. I have upload the KBSO+ logo again for incoporate in the card. in tif and pdf format.

Thank you 

I keep getting request for the logo file. Does everyone has the same problem?

I cannot do much, because the file is upload to the website server. I can't seem to see it either.

The logo file is now working. Please download. I check it myself. Thank you everyone.

Dear All,

Thank you for all the hard work. There are a lot of great work. Due to current commitment with work, I am unable to review them just yet. I will do so next week and advise everyone also. Thank you again. Best regards

Dear All,

Thank you for your participation. There are a lot of good design. Unfortunately, I can only select one. All the best. This is definitely a good crowd to work with. Thank you everyone again.

Best regards

Target Market(s)

Corporate, commercial and institutional projects only

Industry/Entity Type

Business

Requirements
Must have
• elegant simple
double sided with coating
Member of Southland Guild of Draughtsmen (logo only)
corporate colour black and

LOGO FILE UPLOADED
Should not have
• should not be the same as current business card.
upload for reference information only.
font sans serif preferred.

```html
<!DOCTYPE html>
<html lang="en">
<head>
<meta charset="utf-8">
<title>meridale partners business card</title>
<link href="https://fonts.googleapis.com/css2?family=Questrial&display=swap" rel="stylesheet">
<style>
  :root {
    --backdrop: #b4b4b2;
    --card: #1c1c1c;
    --card-edge: #141414;
    --orange: #f0891e;
    --bronze: #6e4519;
    --white: #f2f2f2;
    --rule: #9a9a9a;
  }
  * { margin: 0; padding: 0; box-sizing: border-box; }
  html, body {
    width: 1200px; height: 1000px; overflow: hidden;
    background: var(--backdrop);
    font-family: "Questrial", "Century Gothic", sans-serif;
  }
  .canvas { position: relative; width: 1200px; height: 1000px; }
  .card {
    position: absolute; left: 230px; width: 740px; height: 430px;
    background: radial-gradient(ellipse at 40% 40%, #262626 0%, var(--card) 60%, var(--card-edge) 100%);
    overflow: hidden;
  }
  .card--details { top: 40px; }
  .card--brand { top: 520px; }

  /* details side */
  .wordmark {
    position: absolute; left: 50px; top: 44px;
    display: flex; align-items: center; gap: 12px;
    color: var(--orange); font-size: 24px;
  }
  .wordmark__square { width: 22px; height: 22px; background: var(--orange); }
  .divider {
    position: absolute; left: 90px; right: 40px; top: 150px; height: 2px;
    background: linear-gradient(90deg, transparent 0%, var(--rule) 60%, #d8d8d8 100%);
  }
  .contact {
    position: absolute; left: 50px; top: 200px;
    color: var(--white); font-size: 17px; line-height: 24px;
  }
  .contact__web { color: var(--orange); }
  .person {
    position: absolute; right: 40px; top: 176px; text-align: right;
  }
  .person__name {
    color: var(--white); font-size: 30px; letter-spacing: 0.5px;
    padding-bottom: 8px; border-bottom: 2px solid var(--white);
  }
  .person__role { color: var(--orange); font-size: 24px; margin-top: 6px; }
  .address {
    position: absolute; right: 40px; bottom: 40px; text-align: right;
    color: var(--white); font-size: 18px; line-height: 24px;
  }

  /* brand side */
  .brand-name {
    position: absolute; left: 50px; top: 44px;
    color: var(--white); font-size: 40px; letter-spacing: 0.5px;
  }
  .services {
    position: absolute; left: 50px; top: 110px;
    list-style: none; color: var(--orange); font-size: 19px; line-height: 27px;
  }
  .brand-block {
    position: absolute; right: 40px; top: 70px; width: 330px; height: 330px;
    background: var(--bronze);
  }
</style>
</head>
<body>
<main class="canvas">
  <section class="card card--details">
    <div class="wordmark">
      <span class="wordmark__square"></span>
      <span class="wordmark__name">meridale partners</span>
    </div>
    <div class="divider"></div>
    <div class="contact">
      <p>Tel:&nbsp; +612 9400 2718</p>
      <p>Fax: +612 9400 2719</p>
      <p>mail@meridalepartners.com.au</p>
      <p class="contact__web">www.meridalepartners.com.au</p>
    </div>
    <div class="person">
      <p class="person__name">Firstname Lastname</p>
      <p class="person__role">Function</p>
    </div>
    <div class="address">
      <p>Address line one</p>
      <p>Address line two</p>
    </div>
  </section>

  <section class="card card--brand">
    <h1 class="brand-name">meridale partners</h1>
    <ul class="services">
      <li>project managers</li>
      <li>urban designers</li>
      <li>architects</li>
    </ul>
    <div class="brand-block" role="img" aria-label="Large bronze brand emblem area"></div>
  </section>
</main>
</body>
</html>
```